Corvane ridgewell mechanical

I want a full wrap other than the top of the van.
My services include hvac central A/C, heat pumps,
Fresh air systems, as well as beer and soda systems, air compressors and cryogenics. I have a 2013 Talvor kx 3100 van high roof

Residential and commercial

HVAC , air compressors, beer and soda systems

• Image or design that stands out. Looks sleek and original

```html
<!DOCTYPE html>
<html lang="en">
<head>
<meta charset="utf-8">
<title>Corvane Ridgewell Mechanical – Van Wrap Side Panels</title>
<link rel="stylesheet" href="https://fonts.googleapis.com/css2?family=Montserrat:wght@500;700;800;900&display=swap">
<style>
  :root {
    --navy: #0d2f8a;
    --royal: #1c6fe0;
    --cyan: #23b4ea;
    --white: #ffffff;
    --ink: #0b1533;
    --page: #ffffff;
  }
  html, body {
    margin: 0;
    padding: 0;
    width: 1200px;
    height: 1200px;
    overflow: hidden;
    background: var(--page);
  }
  .canvas {
    width: 1200px;
    height: 1200px;
    display: flex;
    flex-direction: column;
    justify-content: center;
    align-items: center;
    gap: 90px;
  }
  .wrap-panel {
    display: block;
    width: 1100px;
    height: 440px;
  }
  .brand-name { font-family: 'Montserrat', sans-serif; font-weight: 900; fill: var(--navy); }
  .brand-sub { font-family: 'Montserrat', sans-serif; font-weight: 700; fill: var(--navy); }
  .tagline { font-family: 'Montserrat', sans-serif; font-weight: 800; fill: var(--ink); }
  .phone { font-family: 'Montserrat', sans-serif; font-weight: 800; fill: var(--ink); }
  .web { font-family: 'Montserrat', sans-serif; font-weight: 500; fill: var(--ink); }
  .services { font-family: 'Montserrat', sans-serif; font-weight: 700; fill: var(--white); }
  .fill-navy { fill: var(--navy); }
  .fill-cyan { fill: var(--cyan); }
  .fill-royal { fill: var(--royal); }
  .fill-white { fill: var(--white); }
</style>
</head>
<body>
<main class="canvas">

  <!-- Wrap option one: angled chevron layout -->
  <svg class="wrap-panel option-chevron" viewBox="0 0 1100 440" aria-label="Van side wrap, chevron layout">
    <defs>
      <linearGradient id="machineryToneA" x1="0" y1="0" x2="0" y2="1">
        <stop offset="0" stop-color="#1a3f9e"/>
        <stop offset="1" stop-color="#0b2772"/>
      </linearGradient>
    </defs>
    <rect class="fill-navy" x="0" y="0" width="1100" height="440"/>
    <rect x="330" y="280" width="770" height="160" fill="url(#machineryToneA)" role="img" aria-label="Faint photo of mechanical equipment and piping"/>
    <polygon class="fill-white front-panel" points="225,70 430,70 330,440 150,440"/>
    <polygon class="fill-royal accent-triangle" points="410,0 520,0 465,120"/>

    <polygon class="fill-white info-band" points="600,40 1100,40 1100,250 650,250 705,185"/>
    <polygon class="fill-navy chevron-frame" points="545,20 575,20 690,185 590,360 365,360"/>
    <polygon class="fill-cyan chevron" points="562,50 655,185 575,335 400,335"/>

    <polygon class="fill-cyan phone-stripe" points="655,258 1100,258 1100,282 642,282"/>
    <rect class="fill-white" x="722" y="256" width="138" height="28"/>
    <rect class="fill-white" x="864" y="256" width="176" height="28"/>

    <circle class="fill-navy brand-mark" cx="860" cy="100" r="28"/>
    <text class="brand-name" x="730" y="168" font-size="32">CORVANE</text>
    <text class="brand-sub" x="742" y="192" font-size="17">Ridgewell Mechanical</text>
    <text class="tagline" x="730" y="216" font-size="15">BE PROACTIVE NOT REACTIVE</text>
    <text class="phone" x="730" y="276" font-size="15">(802) 555-0147</text>
    <rect class="fill-navy" x="864" y="260" width="2" height="20"/>
    <text class="web" x="872" y="275" font-size="11">www.corvaneridgewell.com</text>
    <text class="services" x="720" y="304" font-size="8" textLength="360" lengthAdjust="spacingAndGlyphs">HVAC CENTRAL A/C - HEAT PUMPS - FRESH AIR SYSTEMS - BEER AND SODA SYSTEMS</text>
    <text class="services" x="825" y="317" font-size="8" textLength="150" lengthAdjust="spacingAndGlyphs">AIR COMPRESSORS AND CRYOGENICS</text>

    <g class="social-dots fill-white">
      <circle cx="100" cy="280" r="7"/>
      <circle cx="122" cy="280" r="7"/>
      <circle cx="144" cy="280" r="7"/>
      <circle cx="166" cy="280" r="7"/>
    </g>
  </svg>

  <!-- Wrap option two: horizontal band layout -->
  <svg class="wrap-panel option-bands" viewBox="0 0 1100 440" aria-label="Van side wrap, band layout">
    <defs>
      <linearGradient id="machineryToneB" x1="0" y1="0" x2="0" y2="1">
        <stop offset="0" stop-color="#1a3f9e"/>
        <stop offset="1" stop-color="#0b2772"/>
      </linearGradient>
    </defs>
    <rect class="fill-navy" x="0" y="0" width="1100" height="440"/>
    <rect x="260" y="230" width="840" height="210" fill="url(#machineryToneB)" role="img" aria-label="Faint photo of mechanical equipment and piping"/>
    <polygon class="fill-white info-band" points="300,60 1100,60 1100,230 200,230 230,140"/>
    <rect class="fill-cyan phone-stripe" x="0" y="275" width="1100" height="34"/>
    <rect class="fill-white" x="530" y="270" width="560" height="44"/>

    <circle class="fill-navy brand-mark" cx="505" cy="150" r="58"/>
    <text class="brand-name" x="590" y="130" font-size="40">CORVANE</text>
    <text class="brand-sub" x="630" y="162" font-size="22">Ridgewell Mechanical</text>
    <text class="tagline" x="590" y="192" font-size="20">BE PROACTIVE NOT REACTIVE</text>
    <text class="services" x="470" y="245" font-size="11" textLength="490" lengthAdjust="spacingAndGlyphs">HVAC CENTRAL A/C - HEAT PUMPS - FRESH AIR SYSTEMS - BEER AND SODA SYSTEMS</text>
    <text class="services" x="560" y="261" font-size="11" textLength="220" lengthAdjust="spacingAndGlyphs">AIR COMPRESSORS AND CRYOGENICS</text>
    <text class="phone" x="545" y="301" font-size="23">(802) 555-0147</text>
    <rect class="fill-navy" x="758" y="278" width="2" height="28"/>
    <text class="web" x="775" y="299" font-size="16">www.corvaneridgewell.com</text>

    <g class="social-dots fill-navy">
      <circle cx="140" cy="292" r="8"/>
      <circle cx="164" cy="292" r="8"/>
      <circle cx="188" cy="292" r="8"/>
      <circle cx="212" cy="292" r="8"/>
    </g>
  </svg>

</main>
</body>
</html>
```